Lawyers in the Netherlands website + logo

We are going in 2015 to launch a website where all law firms in the Netherlands and have the opportunity to place an ad program.

The domain name wil be:

kantoorvinder.website

We want a responsive PSD bootstrap twitter 1170 pixel grid.
for the homepage, result page and the detail page of the customer.

This sites we like:
https://www.qorvantis.com/lawyers

https://lawyers.qorvantis.com/lawyer/tim-garsby-7305826

http://solicitordirectory.brevimark.co.uk/
Map of the Netherlands?

http://solicitordirectory.brevimark.co.uk/listing/category-search/commercial
http://www.tandelvo.com.au/find-a-lawyer/banking-finance-law/

```html
<!DOCTYPE html>
<html lang="en">
<head>
<meta charset="utf-8">
<title>Kantoorvinder</title>
<link href="https://fonts.googleapis.com/css2?family=Roboto:ital,wght@0,300;0,400;0,500;1,400&display=swap" rel="stylesheet">
<style>
:root{
  --navy:#0d2a73;
  --navy-deep:#0a2466;
  --blue-btn:#0f36a8;
  --link:#1f3f93;
  --ink:#444;
  --muted:#666;
  --dark-btn:#2c2c2c;
  --topbar:#f2f2f2;
  --footer:#e2e2e2;
  --white:#fff;
}
*{box-sizing:border-box;margin:0;padding:0}
html,body{width:1200px;height:2179px;overflow:hidden}
body{font-family:"Roboto",Arial,sans-serif;color:var(--ink);background:var(--white);position:relative}
.topbar{height:44px;background:var(--topbar);font-size:13px;color:#555;position:relative}
.topbar ul{list-style:none;position:absolute;right:75px;top:14px;display:flex}
.topbar li+li:before{content:"|";margin:0 10px;color:#777}
.site-header{height:75px;position:relative}
.site-title{position:absolute;left:74px;top:18px;font-size:41px;font-weight:400;color:var(--navy);letter-spacing:.5px}
.callus{position:absolute;right:75px;top:27px;font-size:17px;color:#333;display:flex;align-items:center;gap:6px}
.callus b{font-weight:400;color:var(--link)}
.main-nav{height:49px;background:var(--navy);position:relative}
.main-nav ul{list-style:none;display:flex;position:absolute;left:74px;top:18px;font-size:12.5px;color:var(--white);letter-spacing:.3px}
.main-nav li:nth-child(1){width:85px}.main-nav li:nth-child(2){width:109px}.main-nav li:nth-child(3){width:142px}
.main-nav li:nth-child(4){width:127px}.main-nav li:nth-child(5){width:133px}.main-nav li:nth-child(6){width:105px}
.main-nav li:nth-child(7){width:80px}
.search-btn{position:absolute;right:75px;top:8px;width:32px;height:32px;background:#1f45b3;display:flex;align-items:center;justify-content:center}
.hero{height:429px;position:relative;overflow:hidden}
.hero-photo{position:absolute;inset:0;background:linear-gradient(90deg,#c9a57f 0%,#4b4540 20%,#2d2d30 45%,#6b5a48 60%,#2c2a2b 78%,#c9b7a0 100%)}
.hero-box{position:absolute;left:164px;top:198px;width:873px;height:132px;background:rgba(25,25,25,.82)}
.hero-box h1{font-weight:400;font-size:43px;color:var(--white);text-align:center;margin-top:6px;letter-spacing:.5px}
.hero-search{position:absolute;left:17px;top:61px;width:839px;height:55px;background:var(--white);display:flex;align-items:center}
.hero-search .field{font-style:italic;font-size:14px;color:#777;padding-left:18px;height:100%;display:flex;align-items:center}
.hero-search .issue{width:308px;border-right:1px solid #ddd}
.hero-search .city{flex:1}
.hero-search .btn{width:121px;height:43px;margin-right:11px;background:var(--blue-btn);color:var(--white);font-size:18px;display:flex;align-items:center;justify-content:center}
.dots{position:absolute;left:562px;top:392px;display:flex;gap:8px}
.dots i{width:13px;height:13px;border-radius:50%;background:#111}
.dots i:first-child{background:var(--white)}
h2.sec{font-weight:400;font-size:23px;color:var(--navy);letter-spacing:.3px}
.welcome{height:305px;position:relative}
.welcome .text{position:absolute;left:74px;top:35px;width:685px}
.welcome p{font-size:11.2px;line-height:23px;color:var(--ink)}
.welcome h2{margin-bottom:10px}
.welcome p+p{margin-top:6px}
.btn-dark{display:inline-flex;align-items:center;justify-content:center;width:135px;height:40px;background:var(--dark-btn);color:var(--white);font-size:14px;letter-spacing:.3px;border-radius:2px}
.welcome .btn-dark{position:absolute;left:74px;top:235px}
.video{position:absolute;left:795px;top:35px;width:330px}
.video-frame{margin-top:10px;width:330px;height:198px;border:2px solid #ccc;background:linear-gradient(135deg,#6d665c,#c9c4bb 45%,#8e887d);display:flex;align-items:center;justify-content:center}
.services{height:381px;position:relative;background:var(--navy);overflow:hidden;color:var(--white)}
.services svg.art{position:absolute;inset:0}
.services .text{position:absolute;left:74px;top:30px;width:610px}
.services h2{color:var(--white);margin-bottom:12px}
.services p{font-size:11.2px;line-height:18.5px;font-weight:300}
.services ul{list-style:none;margin-top:16px}
.services li{font-size:11.2px;font-weight:300;height:24px;display:flex;align-items:center;gap:10px}
.services .btn-dark{position:absolute;left:74px;top:318px}
.partners{height:199px;text-align:center}
.partners h2{font-size:22px;font-weight:400;color:var(--navy);padding-top:58px}
.partner-row{display:flex;justify-content:center;gap:58px;margin-top:26px;align-items:center}
.partner-row span{display:block;width:120px;height:28px;background:#d2d2d2;border-radius:3px}
.features{height:311px;background:var(--navy-deep);color:var(--white);display:flex;padding-left:74px}
.feature{width:361px;text-align:center;padding-top:47px}
.feature:nth-child(1){margin-left:-3px}
.feature h3{font-weight:500;font-size:19px;letter-spacing:.4px;margin-top:23px;white-space:nowrap}
.feature p{font-size:13px;line-height:26px;margin-top:9px;padding:0 48px}
.bottom{height:267px;position:relative}
.news{position:absolute;left:74px;top:34px;width:485px}
.news p{font-size:11.5px;line-height:21px;color:var(--ink);margin-top:12px}
.news .date{font-size:11.5px;color:var(--link);margin-top:6px;margin-bottom:20px}
.news h2+p{margin-top:18px}
.clients{position:absolute;left:614px;top:34px;width:511px}
.quote{display:flex;gap:8px;margin-top:18px}
.quote svg{flex:none;margin-top:2px}
.quote p{font-size:11.2px;line-height:21px;font-style:italic;color:var(--muted)}
.client{display:flex;align-items:center;gap:14px;margin-top:28px}
.client-photo{width:62px;height:62px;background:linear-gradient(#e8e4df,#3a3a3a)}
.client b{display:block;font-weight:500;font-size:11.5px;color:var(--link)}
.client i{font-size:11px;color:var(--muted)}
.site-footer{height:119px;background:var(--footer);position:relative}
.footer-links{position:absolute;left:74px;top:38px;font-size:11.5px;color:#333}
.footer-links span{margin:0 9px}
.copy{position:absolute;left:74px;top:64px;font-size:11px;color:#666}
.connect{position:absolute;right:75px;top:37px;display:flex;align-items:center;gap:6px;font-size:17px;color:#444}
.connect .label{margin-right:8px}
.connect i{width:30px;height:30px;border-radius:50%;background:var(--link)}
</style>
</head>
<body>
<div class="topbar">
  <ul><li>Find a Lawyer</li><li>Legal Answers</li><li>Law &nbsp;More</li><li>Sign In</li><li>Lawyers Get Listed</li><li>FAQ</li></ul>
</div>
<header class="site-header">
  <div class="site-title">Kantoorvinder</div>
  <div class="callus">
    <svg width="17" height="17" viewBox="0 0 17 17"><rect width="17" height="17" rx="3" fill="#333"/><path d="M5 4c1 0 1.6 2 1.6 2.5S5.7 7.6 5.9 8.3c.5 1.3 1.6 2.4 2.8 2.8.7.2 1.3-.7 1.8-.7s2.5.6 2.5 1.6S11.8 14 10.9 14C7 14 3 10 3 6.1 3 5.2 4 4 5 4z" fill="#fff"/></svg>
    Call Us: <b>123-456-7890</b>
  </div>
</header>
<nav class="main-nav">
  <ul><li>HOME</li><li>ABOUT US</li><li>PRACTICE AREA</li><li>ADVOCATES</li><li>LATEST NEWS</li><li>CAREERS</li><li>BLOG</li><li>CONTACT US</li></ul>
  <div class="search-btn"><svg width="16" height="16" viewBox="0 0 16 16"><circle cx="6" cy="6" r="4.2" fill="none" stroke="#fff" stroke-width="2"/><path d="M9 9l5 5" stroke="#fff" stroke-width="2.4" stroke-linecap="round"/></svg></div>
</nav>
<section class="hero">
  <div class="hero-photo" role="img" aria-label="Photo of two smiling lawyers in business suits in an office"></div>
  <div class="hero-box">
    <h1>Helping You With Your Legal Needs</h1>
    <div class="hero-search">
      <div class="field issue">Search Legal Issue</div>
      <div class="field city">Enter City</div>
      <div class="btn">SEARCH</div>
    </div>
  </div>
  <div class="dots"><i></i><i></i><i></i><i></i></div>
</section>
<section class="welcome">
  <div class="text">
    <h2 class="sec">WELCOME TO OUR WEBSITE</h2>
    <p>Aliquam molestie, mi et imperdiet euismod, dui purus auctor tellus, et interdum lacus lectus et ante. Sed accumsan sollicitudin sapien, sit amet adipiscing turpis gravida ac. In congue, neque ac lobortis volutpat, libero mauris varius mi, vitae suscipit ipsum ligula vitae risus. Duis aliquam nibh a dui iaculis viverra id a velit. Vivamus egestas risus in magna varius commodo. Sed semper viverra egestas. Etiam pretium porttitor lectus, vel ornare neque porta volutpat.</p>
    <p>Aenean a nibh eget turpis vehicula tempus ac sed massa. Vestibulum dolor nulla, ultrices ac tincidunt sed, laoreet non est. Suspendisse lobortis turpis in odio blandit ac interdum lorem euismod.</p>
  </div>
  <a class="btn-dark">READ MORE</a>
  <div class="video">
    <h2 class="sec">VIDEO</h2>
    <div class="video-frame" role="img" aria-label="Video still of legal documents and glasses on a desk">
      <svg width="62" height="62" viewBox="0 0 62 62"><circle cx="31" cy="31" r="28" fill="rgba(0,0,0,.25)" stroke="#fff" stroke-width="3"/><path d="M24 17l20 14-20 14z" fill="#fff"/></svg>
    </div>
  </div>
</section>
<section class="services">
  <svg class="art" width="1200" height="381" viewBox="0 0 1200 381">
    <defs><linearGradient id="gavel" x1="0" y1="0" x2="1" y2="1"><stop offset="0" stop-color="#8a5a3a"/><stop offset=".5" stop-color="#4a2a1c"/><stop offset="1" stop-color="#b07a4e"/></linearGradient></defs>
    <path d="M763 0H1200V381H392C520 320 720 200 763 0Z" fill="url(#gavel)" role="img" aria-label="Photo of a wooden judge's gavel resting on law books"/>
    <path d="M392 381C520 320 720 200 763 0" fill="none" stroke="#1d4fc4" stroke-width="6"/>
  </svg>
  <div class="text">
    <h2 class="sec">OUR SERVICES</h2>
    <p>Aliquam molestie, mi et imperdiet euismod, dui purus auctor tellus, et interdum lacus lectus et ante. Sed accumsan sollicitudin sapien, sit amet adipiscing turpis gravida ac. In congue, neque ac lobortis Duis aliquam nibh a dui iaculis viverra id a velit.</p>
    <ul>
      <li><svg width="11" height="9" viewBox="0 0 11 9"><path d="M1 5l3 3 6-7" fill="none" stroke="#fff" stroke-width="2"/></svg>Vivamus egestas risus in magna varius commodo</li>
      <li><svg width="11" height="9" viewBox="0 0 11 9"><path d="M1 5l3 3 6-7" fill="none" stroke="#fff" stroke-width="2"/></svg>Sed semper viverra egestas</li>
      <li><svg width="11" height="9" viewBox="0 0 11 9"><path d="M1 5l3 3 6-7" fill="none" stroke="#fff" stroke-width="2"/></svg>Etiam pretium porttitor lectus</li>
      <li><svg width="11" height="9" viewBox="0 0 11 9"><path d="M1 5l3 3 6-7" fill="none" stroke="#fff" stroke-width="2"/></svg>Vel ornare neque porta volutpat</li>
      <li><svg width="11" height="9" viewBox="0 0 11 9"><path d="M1 5l3 3 6-7" fill="none" stroke="#fff" stroke-width="2"/></svg>Aenean a nibh eget turpis vehicula tempus</li>
      <li><svg width="11" height="9" viewBox="0 0 11 9"><path d="M1 5l3 3 6-7" fill="none" stroke="#fff" stroke-width="2"/></svg>Vestibulum dolor nulla</li>
    </ul>
  </div>
  <a class="btn-dark">READ MORE</a>
</section>
<section class="partners">
  <h2>Premium Partners of the Lawyers Network:</h2>
  <div class="partner-row" aria-label="Partner badges"><span></span><span></span><span></span><span></span><span></span></div>
</section>
<section class="features">
  <div class="feature">
    <svg width="110" height="110" viewBox="0 0 110 110"><circle cx="55" cy="55" r="53" fill="none" stroke="#fff" stroke-width="2.5"/><path d="M30 52l14-14 10 8 10-8 16 14-20 18-8-6-6 6z" fill="none" stroke="#fff" stroke-width="3" stroke-linejoin="round"/><path d="M46 58l8 6M52 52l8 6" stroke="#fff" stroke-width="2.5"/></svg>
    <h3>QORVANTIS LAWYER DIRECTORY</h3>
    <p>Nemo enim ipsam voluptatem voluptas sit aspernatur aut oditaut.</p>
  </div>
  <div class="feature">
    <svg width="110" height="110" viewBox="0 0 110 110"><circle cx="55" cy="55" r="53" fill="none" stroke="#fff" stroke-width="2.5"/><path d="M55 28l5 6 7-2 1 7 7 3-3 7 3 7-7 3-1 7-7-2-5 6-5-6-7 2-1-7-7-3 3-7-3-7 7-3 1-7 7 2z" fill="none" stroke="#fff" stroke-width="2.5" stroke-linejoin="round"/><path d="M46 70l-6 14 8-3 4 7 3-10M64 70l6 14-8-3-4 7-3-10" fill="none" stroke="#fff" stroke-width="2.5" stroke-linejoin="round"/></svg>
    <h3>QORVANTIS LAWYER DIRECTORY</h3>
    <p>Nemo enim ipsam voluptatem voluptas sit aspernatur aut oditaut.</p>
  </div>
  <div class="feature">
    <svg width="110" height="110" viewBox="0 0 110 110"><circle cx="55" cy="55" r="53" fill="none" stroke="#fff" stroke-width="2.5"/><path d="M55 30v44M42 76h26M34 40h42" stroke="#fff" stroke-width="2.5" stroke-linecap="round"/><path d="M34 40l-8 18h16zM76 40l-8 18h16zM26 58a8 5 0 0016 0M68 58a8 5 0 0016 0" fill="none" stroke="#fff" stroke-width="2.5" stroke-linejoin="round"/></svg>
    <h3>QORVANTIS LAWYER DIRECTORY</h3>
    <p>Nemo enim ipsam voluptatem voluptas sit aspernatur aut oditaut.</p>
  </div>
</section>
<section class="bottom">
  <div class="news">
    <h2 class="sec">LATEST NEWS</h2>
    <p>Aliquam molestie, mi et imperdiet euismod, dui purus auctor tellus, et interdum lacus lectus et ante. Sed accumsan sollicitudin sapien, sit amet adipiscing turpis gravida ac.</p>
    <p class="date">Posted on Jan28, 2015</p>
    <p>Aliquam molestie, mi et imperdiet euismod, dui purus auctor tellus, et interdum lacus lectus et ante. Sed accumsan sollicitudin sapien, sit amet adipiscing turpis gravida ac.</p>
    <p class="date">Posted on Jan28, 2015</p>
  </div>
  <div class="clients">
    <h2 class="sec">WHAT OUR CLIENT SAYS...</h2>
    <div class="quote">
      <svg width="30" height="14" viewBox="0 0 30 14"><path d="M2 13c0-6 3-10 9-12v3c-3 1-4 3-4 5h4v4zM17 13c0-6 3-10 9-12v3c-3 1-4 3-4 5h4v4z" fill="#bbb"/></svg>
      <p>Aliquam molestie, mi et imperdiet euismod, dui purus auctor tellus, et interdum lacus lectus et ante. Sed accumsan sollicitudin sapien, sit amet adipiscing turpis gravida ac. Consectetuer adipiscing elit, sed diam nonummy nibh euismod tincidunt.</p>
    </div>
    <div class="client">
      <div class="client-photo" role="img" aria-label="Client portrait photo"></div>
      <div><b>Name Goes here</b><i>Location</i></div>
    </div>
  </div>
</section>
<footer class="site-footer">
  <div class="footer-links">Company Terms of Service<span>/</span>Privacy Policy<span>/</span>Contact Us</div>
  <div class="copy">Copyright © 2015. CompanyName. All Right Reserved</div>
  <div class="connect"><span class="label">Connect Us:</span><i aria-label="Social link"></i><i aria-label="Social link"></i><i aria-label="Social link"></i><i aria-label="Social link"></i></div>
</footer>
</body>
</html>
```